E-Commerce startup needs a Brellix store front

Tallow are looking for help designing and building a Brellix store front.

So what do we need?

A simple, user-friendly home page to display menu options and collections of products.

It’s got to be clean. Uncluttered.

No screaming starbursts! No sale countdown timers.

Clean.

Functional. Clean.

Looks great in mobile. Clean.

Clean but not cold. Needs personality. Design should cue trust and quality.

How it will work is this: every update cycle, we’ll add 5 new products to the site. 5 umbrellas, 5 travel mugs, 5 candle holders, etc. We will need a key frame that will hold an image and a headline. We want these frames to feel consistent from one product to the next. It’s important to note that the headlines are key to personality of the site and their treatment should not be overlooked.

Consistent headline style
Consistent background type (solo product or product in-situ)
Consistent branding cues

While these product frames will be the meat of the site, there are other considerations, as well.

When we click on a product key frame, it will take us to a page with that product collection. There will be the 5 products with supporting copy (product details/specs) and images for each. What should this page look like?

What should the header/navigation look like?

What about the footer?

How about the feature image on home/landing page?

How should we handle copy heavy pages (About us, Shipping policy, returns, etc)

Guidelines:
Colour palette to be based on logo but can expand from there.
San-serif fonts
Needs to work across popular devices (mobile/desktop/tablet) and operating systems. With flexibility to expand into an app in the future.

Some multi-category sites we like:

Quorvane.com – Clean header, design and colours feel warm, friendly
Delphwick.com – The rounded feature boxes are cheerful, inviting
Pell.co.uk – Large images, nice photography, stylish consistent

Some sites we don’t love the look of

Rimu.co.uk – Products photos are too inconsistent in size, shape and style. Looks messy.
Zoba.com – Too many sale offers, pop ups, deals, deals, deals. Feels cheap and desperate.
Frandle.co.uk – Feels like an overwhelming amount of information and boxes.

Please feel free to contact us with questions.

Thank you for your designs and expertise. Looking forward to seeing your work.

```html
<!DOCTYPE html>
<html lang="en">
<head>
<meta charset="utf-8">
<title>Tallow — Home</title>
<link href="https://fonts.googleapis.com/css2?family=Mulish:wght@400;500;600;700;800;900&family=Poppins:wght@600;700&display=swap" rel="stylesheet">
<style>
:root{
  --red:#e8403a;
  --yellow:#fdb813;
  --ink:#1d1d1d;
  --field:#f0f0f0;
  --white:#fff;
  --footer:#000;
  --footer-text:#e6e6e6;
}
*{box-sizing:border-box;margin:0;padding:0}
html,body{width:1200px;height:2538px;overflow:hidden}
body{font-family:"Mulish",sans-serif;color:var(--ink);background:var(--white);position:relative}
a{color:inherit;text-decoration:none}

.site-header{height:95px;display:flex;align-items:center;padding:0 0 0 133px;position:relative}
.brand{font-weight:900;color:var(--red);font-size:44px;letter-spacing:-1px;line-height:1}
.search{position:absolute;left:410px;top:28px;width:331px;height:43px;background:var(--field);border-radius:8px;display:flex;align-items:center;justify-content:space-between;padding:0 16px;font-size:13px;color:#555}
.header-actions{position:absolute;left:783px;top:38px;display:flex;align-items:center;gap:40px;font-size:14px;color:#333}
.header-actions span{display:flex;align-items:center;gap:9px}
.cart{position:relative}
.cart-count{position:absolute;top:-8px;right:-8px;width:14px;height:14px;border-radius:50%;background:var(--red);color:#fff;font-size:9px;font-weight:400;display:flex;align-items:center;justify-content:center}

.main-nav{height:41px;background:var(--red);display:flex;align-items:center;padding-left:137px;color:#fff;font-weight:700;font-size:14.5px}
.main-nav a:nth-child(1){width:160px}.main-nav a:nth-child(2){width:164px}.main-nav a:nth-child(3){width:86px}
.main-nav a:nth-child(4){width:89px}.main-nav a:nth-child(5){width:106px}.main-nav a:nth-child(6){width:89px}
.main-nav a:nth-child(7){width:114px}.main-nav a:nth-child(8){width:92px}

.hero{height:657px;position:relative;text-align:center;overflow:hidden}
.hero-media{position:absolute;inset:0;
  background:
    radial-gradient(ellipse 110px 330px at 150px 300px,rgba(108,140,90,.75),rgba(108,140,90,0) 100%),
    radial-gradient(ellipse 120px 130px at 150px 570px,rgba(214,120,70,.95),rgba(214,120,70,0) 100%),
    radial-gradient(ellipse 260px 180px at 1000px 70px,rgba(140,170,90,.55),rgba(140,170,90,0) 100%),
    radial-gradient(ellipse 90px 140px at 1010px 470px,rgba(150,175,80,.7),rgba(150,175,80,0) 100%),
    radial-gradient(ellipse 90px 90px at 760px 590px,rgba(200,200,196,.9),rgba(200,200,196,0) 100%),
    radial-gradient(ellipse 90px 120px at 850px 570px,rgba(210,110,60,.85),rgba(210,110,60,0) 100%),
    radial-gradient(ellipse 80px 100px at 920px 600px,rgba(160,165,150,.85),rgba(160,165,150,0) 100%),
    radial-gradient(ellipse 80px 110px at 1090px 590px,rgba(130,140,80,.85),rgba(130,140,80,0) 100%),
    linear-gradient(180deg,#f7f6f4 0%,#efedea 60%,#e3e0dc 88%,#c9a57c 92%,#b88f63 100%);}
.hero-copy{position:absolute;left:0;right:0;top:172px}
.hero h1{font-weight:900;font-size:62px;color:var(--red);letter-spacing:0.5px;line-height:1}
.hero p{margin-top:26px;font-size:20px;line-height:29px;color:#333}
.btn{display:inline-block;margin-top:28px;background:var(--yellow);color:#fff;font-weight:800;font-size:19px;padding:13px 28px;border-radius:9px}

.feature-row{display:flex;justify-content:space-between;padding:0 9px 0 14px;margin-top:16px}
.feature-card{width:384px;height:457px;border-radius:8px;position:relative;overflow:hidden}
.feature-card::after{content:"";position:absolute;inset:0;background:linear-gradient(180deg,rgba(0,0,0,0) 65%,rgba(0,0,0,.4) 100%)}
.feature-card h3{position:absolute;left:31px;bottom:24px;right:10px;color:#fff;font-weight:500;font-size:19.5px;line-height:28px;z-index:1;white-space:nowrap}

.card-charger{background:
  radial-gradient(ellipse 130px 150px at 190px 230px,rgba(30,30,32,.95),rgba(30,30,32,0) 100%),
  radial-gradient(ellipse 200px 160px at 330px 260px,rgba(170,130,90,.9),rgba(170,130,90,0) 100%),
  linear-gradient(160deg,#a8a8a6 0%,#8e8c89 55%,#7a624a 100%)}
.card-toys{background:
  radial-gradient(ellipse 80px 120px at 80px 220px,rgba(220,90,150,.8),rgba(220,90,150,0) 100%),
  radial-gradient(ellipse 90px 140px at 280px 180px,rgba(245,200,200,.9),rgba(245,200,200,0) 100%),
  radial-gradient(ellipse 80px 80px at 195px 310px,rgba(235,235,235,.85),rgba(235,235,235,0) 100%),
  radial-gradient(ellipse 90px 110px at 320px 330px,rgba(200,150,190,.8),rgba(200,150,190,0) 100%),
  linear-gradient(180deg,#ea8fae 0%,#e28aa6 70%,#c77d92 100%)}
.card-chair{background:
  radial-gradient(ellipse 90px 150px at 200px 220px,rgba(200,30,40,.75),rgba(200,30,40,0) 100%),
  radial-gradient(ellipse 20px 80px at 68px 90px,rgba(230,80,240,.8),rgba(230,80,240,0) 100%),
  radial-gradient(ellipse 20px 80px at 322px 90px,rgba(230,80,240,.8),rgba(230,80,240,0) 100%),
  radial-gradient(circle at 50% 45%,#3a1035 0%,#1c0820 55%,#0d0410 100%)}
.card-collar{background:
  radial-gradient(ellipse 150px 220px at 200px 230px,rgba(250,250,250,.95),rgba(250,250,250,0) 100%),
  radial-gradient(ellipse 90px 90px at 200px 80px,rgba(70,60,55,.7),rgba(70,60,55,0) 100%),
  linear-gradient(160deg,#d8dadc 0%,#c2c2bf 60%,#8a8580 100%)}
.card-cheese{background:
  radial-gradient(ellipse 150px 110px at 190px 220px,rgba(190,130,80,.95),rgba(190,130,80,0) 100%),
  radial-gradient(ellipse 60px 50px at 250px 180px,rgba(245,215,80,.85),rgba(245,215,80,0) 100%),
  linear-gradient(160deg,#959998 0%,#7a7e7c 60%,#5e5f5c 100%)}
.card-box{background:
  radial-gradient(ellipse 170px 170px at 180px 240px,rgba(170,220,222,1),rgba(170,220,222,0) 100%),
  radial-gradient(ellipse 90px 25px at 190px 110px,rgba(40,100,210,.9),rgba(40,100,210,0) 100%),
  linear-gradient(170deg,#4c4c4e 0%,#5e5e60 60%,#6b5040 100%)}

.categories{text-align:center;margin-top:44px}
.categories h2{font-family:"Poppins",sans-serif;font-weight:700;font-size:28px;letter-spacing:0.3px}
.rule{width:42px;height:3px;background:var(--red);margin:17px auto 0}
.cat-list{position:relative;height:220px;margin-top:36px}
.cat{position:absolute;top:0;width:160px;text-align:center}
.cat .thumb{width:145px;height:145px;border-radius:50%;margin:0 auto}
.cat span{display:block;margin-top:25px;font-weight:700;font-size:15px}

.feature-row.second{margin-top:24px}

.site-footer{position:absolute;left:0;top:2118px;width:1200px;height:420px;background:var(--footer);color:var(--footer-text)}
.footer-brand{position:absolute;left:133px;top:50px;font-weight:900;color:var(--red);font-size:84px;letter-spacing:-2px;line-height:1}
.follow{position:absolute;left:152px;top:215px;display:flex;align-items:center;gap:24px}
.follow h4{color:var(--red);font-weight:800;font-size:17px}
.social{display:flex;gap:12px;font-size:13px;font-weight:600;color:#fff}
.social span{display:flex;align-items:center;gap:6px}
.social i{width:16px;height:16px;border-radius:3px;background:var(--red);display:inline-block}
.col{position:absolute;top:52px}
.col h5{color:var(--red);font-weight:700;font-size:17px;margin-bottom:11px}
.col li{list-style:none;font-size:13px;line-height:22.4px}
.divider{position:absolute;left:133px;width:936px;top:320px;height:1px;background:#3a3a3a}
.copyright{position:absolute;top:362px;left:0;right:0;text-align:center;font-size:13px}
</style>
</head>
<body>

<header class="site-header">
  <a class="brand" href="#">Tallow</a>
  <div class="search">Search
    <svg width="14" height="14" viewBox="0 0 14 14" fill="none" stroke="#555" stroke-width="1.4"><circle cx="6" cy="6" r="4.5"/><path d="M9.5 9.5L13 13"/></svg>
  </div>
  <div class="header-actions">
    <span><svg width="18" height="16" viewBox="0 0 18 16" fill="none" stroke="#333" stroke-width="1.4"><path d="M11 1h5v14h-5M1 8h10M7 4l4 4-4 4"/></svg>Sign In</span>
    <span><svg width="20" height="20" viewBox="0 0 20 20" fill="none" stroke="#333" stroke-width="1.4"><circle cx="10" cy="10" r="9"/><circle cx="10" cy="8" r="3"/><path d="M4.5 16c1.5-2.5 9.5-2.5 11 0"/></svg>My Account</span>
    <span class="cart"><svg width="20" height="20" viewBox="0 0 20 20" fill="none" stroke="#333" stroke-width="1.4"><path d="M3 5h14l-1.5 12h-11z"/><path d="M7 8V4a3 3 0 016 0v4"/></svg><b class="cart-count">0</b></span>
  </div>
</header>

<nav class="main-nav">
  <a href="#">Home &amp; Garden</a><a href="#">Sport &amp; Fitness</a><a href="#">Pets</a><a href="#">Kids</a><a href="#">Babies</a><a href="#">Men</a><a href="#">Women</a><a href="#">Gifts</a><a href="#">New</a>
</nav>

<section class="hero">
  <div class="hero-media" role="img" aria-label="Potted cactus and succulents on a wooden shelf with trailing plants hanging from above"></div>
  <div class="hero-copy">
    <h1>HOUSE PLANTS</h1>
    <p>Lorem ipsum dolor sit amet, consectetur adipiscing<br>elit, sed do eiusmod tempor incididunt ut lab.</p>
    <a class="btn" href="#">SHOP NOW</a>
  </div>
</section>

<section class="feature-row">
  <article class="feature-card card-charger" role="img" aria-label="Black portable charger with cable on a concrete surface">
    <h3>5 portable chargers FOR when<br>mum needs a quick chat</h3>
  </article>
  <article class="feature-card card-toys" role="img" aria-label="Soft plush toys on a pink background">
    <h3>5 sensory toys FOR babies<br>that are easily amazed</h3>
  </article>
  <article class="feature-card card-chair" role="img" aria-label="Red and black gaming chair under purple neon lights">
    <h3>5 gaming chairs FOR heroes<br>with princesses to save</h3>
  </article>
</section>

<section class="categories">
  <h2>CATEGORIES</h2>
  <div class="rule"></div>
  <div class="cat-list">
    <a class="cat" href="#" style="left:16px"><div class="thumb" role="img" aria-label="House with a green garden" style="background:radial-gradient(circle at 50% 75%,#6f9a3a 0%,#8aa86a 45%,#c8d4d8 100%)"></div><span>Home &amp; Garden</span></a>
    <a class="cat" href="#" style="left:181px"><div class="thumb" role="img" aria-label="Person training with kettlebells" style="background:radial-gradient(circle at 55% 50%,#c79a80 0%,#6e7b88 55%,#3f4954 100%)"></div><span>Sport &amp; Fitness</span></a>
    <a class="cat" href="#" style="left:351px"><div class="thumb" role="img" aria-label="Cat and dog sitting on grass" style="background:radial-gradient(circle at 55% 50%,#d49a5a 0%,#9c8a5a 45%,#5e8f2e 100%)"></div><span>Pets</span></a>
    <a class="cat" href="#" style="left:522px"><div class="thumb" role="img" aria-label="Wooden chest full of toys" style="background:radial-gradient(circle at 50% 40%,#e0a060 0%,#4aa4c8 60%,#6a4a2a 100%)"></div><span>Kids</span></a>
    <a class="cat" href="#" style="left:696px"><div class="thumb" role="img" aria-label="Two sleeping babies in knitted hats" style="background:radial-gradient(circle at 50% 55%,#f0c8b8 0%,#d8c6cc 55%,#9fb8d0 100%)"></div><span>Babies</span></a>
    <a class="cat" href="#" style="left:864px"><div class="thumb" role="img" aria-label="Men in tailored suits" style="background:radial-gradient(circle at 50% 60%,#d8c8a8 0%,#a89070 50%,#3e5a3a 100%)"></div><span>Men</span></a>
    <a class="cat" href="#" style="left:1032px"><div class="thumb" role="img" aria-label="Woman in a beige dress" style="background:radial-gradient(circle at 45% 60%,#a07a5e 0%,#c8a890 45%,#ece6de 100%)"></div><span>Women</span></a>
  </div>
</section>

<section class="feature-row second">
  <article class="feature-card card-collar" role="img" aria-label="Dog wearing a colourful collar">
    <h3>5 brilliant collars FOR budget<br>conscious border collies</h3>
  </article>
  <article class="feature-card card-cheese" role="img" aria-label="Cheese board with nuts and herbs on grey stone">
    <h3>5 cheese boards FOR<br>asiago aficionados</h3>
  </article>
  <article class="feature-card card-box" role="img" aria-label="Light blue metal lunch box with fruit pictures">
    <h3>5 fun storage containers FOR<br>your children to throw things near</h3>
  </article>
</section>

<footer class="site-footer">
  <div class="footer-brand">Tallow</div>
  <div class="follow">
    <h4>FOLLOW US</h4>
    <div class="social"><span><i></i>Flock</span><span><i></i>Snapia</span></div>
  </div>
  <div class="col" style="left:523px">
    <h5>LINKS</h5>
    <ul><li>About Us</li><li>FAQ</li><li>Contact US</li><li>Terms of Service</li><li>Return Policy</li><li>Shipping Policy</li><li>Track My Order</li></ul>
  </div>
  <div class="col" style="left:745px">
    <h5>MENUS</h5>
    <ul><li>Volunteer</li><li>Foundation</li><li>Events</li><li>News</li><li>The Pavilion</li><li>Shop</li></ul>
  </div>
  <div class="col" style="left:941px">
    <h5>CATEGORIES</h5>
    <ul><li>Home &amp; Garden</li><li>Sport &amp; Fitness</li><li>Pets</li><li>Kids</li><li>Babies</li><li>Men</li><li>Women</li><li>Gifts</li><li>New</li></ul>
  </div>
  <div class="divider"></div>
  <p class="copyright">Copyright © 2024 All Rights Reserved</p>
</footer>

</body>
</html>
```